Christmas social media advert post

I am looking for an eye catching advert for use mainly on social media posts.
The following is the detail of the event.

Christmas special offer-
£10pp,– offer includes –
Half an hour Toboggan track,
Half an hour Slingshot paintballs (20 paintballs pp) and safe target archery (under cover and indoor ranges). Activities all the family from age 4 to grandparents can join in,
Also available – Add on indoor activities including Mini Curling, Bead Blitz, Safe axe throwing, Air juggler – from £3.50pp and age 6plus
Café open for hot food and drinks in the ‘Fireside Frost Lodge and the heated Christmas marquee.

A basic idea I put together for what I feel is the important information is -

Christmas Special offer -
Starts Saturday 20th December.
£10pp – offer includes –
Half an hour Slingshot paintballs (20 paintballs pp) and safe target archery (under cover and indoor ranges). Activities all the family from age 4 to grandparents can join in. Booking is essential - details on how below.
Also available Add on indoor activities - including Mini Curling, Bead Blitz, Safe axe throwing, Air juggler – from £3.50pp and age 6plus.
Ages start from 4 plus.
All activities are great for children and adults so perfect for families as well as friends, parties and get togethers.
Free huge car parks,
Booking is easy-
Just Message from our chat (on this post) or email
martin@hollowbrookleisurepark.co.uk for availability of your preferred date and time.

I would be happy to send the detailed information to enquiries if it meant a better looking advert / post.

Full details are in the picture uploads, feel free to use as much or as little of the information as you feel best.

```html
<!DOCTYPE html>
<html lang="en">
<head>
<meta charset="utf-8">
<title>Christmas Special Offer</title>
<link rel="stylesheet" href="https://fonts.googleapis.com/css2?family=Poppins:wght@300;400;500;600;700&family=Great+Vibes&family=Playfair+Display:ital,wght@0,600;1,700&display=swap">
<style>
  :root {
    --backdrop: #e2e2e2;
    --paper: #ffffff;
    --festive-red: #e3333f;
    --deep-red: #9b0a12;
    --banner-red: #c60b18;
    --gold: #e0b655;
    --gold-text: #c49a45;
    --ink: #3f3f3f;
    --ink-dark: #111111;
    --email-yellow: #ffd21a;
  }
  * { margin: 0; padding: 0; box-sizing: border-box; }
  html, body { width: 869px; height: 1200px; overflow: hidden; background: var(--backdrop); }
  body { position: relative; font-family: "Poppins", sans-serif; }

  .flyer {
    position: absolute; left: 85px; top: 98px; width: 699px; height: 1006px;
    background: var(--paper); overflow: hidden;
  }
  .abs { position: absolute; }
  .center-text { left: 0; right: 0; text-align: center; }

  .garland {
    left: 0; top: 0; width: 699px; height: 230px;
    background: linear-gradient(180deg, #7fb83a 0%, #a9cf6e 28%, #dfe6d4 58%, rgba(255,255,255,0) 100%);
  }
  .script-title {
    top: 132px; font-family: "Great Vibes", cursive; font-size: 54px;
    color: var(--festive-red); line-height: 1;
  }
  .main-title {
    top: 188px; font-weight: 700; font-size: 71px; letter-spacing: -1px;
    color: var(--festive-red); line-height: 1;
  }

  .date-banner {
    left: 31px; top: 286px; width: 606px; height: 120px; border-radius: 42px;
    background: linear-gradient(100deg, #a00812 0%, var(--banner-red) 45%, #8f0510 100%);
    overflow: hidden;
  }
  .banner-pine {
    left: 0; top: 0; width: 130px; height: 120px;
    background: linear-gradient(110deg, #3d6b4a 0%, rgba(61,107,74,0.4) 50%, rgba(61,107,74,0) 100%);
  }
  .banner-glow {
    right: 0; top: 0; width: 110px; height: 120px;
    background: linear-gradient(90deg, rgba(224,182,85,0) 0%, rgba(224,182,85,0.35) 60%, rgba(224,182,85,0.6) 100%);
  }
  .starts-tab {
    left: 151px; top: 0; width: 335px; height: 32px; border-radius: 0 0 18px 18px;
    background: linear-gradient(90deg, #c49738, var(--gold) 30%, var(--gold) 70%, #c49738);
    text-align: center; font-family: "Playfair Display", serif; font-weight: 600;
    font-size: 31px; line-height: 34px; color: #fff8e8;
  }
  .date-row {
    left: 0; right: 0; top: 32px; display: flex; justify-content: center;
    align-items: center; gap: 12px; color: #fff;
  }
  .date-word { font-weight: 600; font-size: 24px; }
  .date-day { font-family: "Great Vibes", cursive; font-size: 86px; line-height: 1; }

  .price {
    top: 418px; left: 0; width: 672px; font-weight: 700; font-size: 54px;
    color: var(--gold-text); line-height: 1; text-align: center; letter-spacing: -1px;
  }
  .includes-label { top: 478px; font-weight: 600; font-size: 21px; color: var(--ink); }
  .includes-rule { border-top: 1px solid #9a6a3a; height: 0; }
  .includes-tick { border-left: 1px solid #9a6a3a; width: 0; }

  .offer-box {
    top: 516px; height: 87px; background: var(--gold); color: #fff;
    display: flex; flex-direction: column; justify-content: center; align-items: center;
    text-align: center; line-height: 1.2;
  }
  .offer-box--left { left: 71px; width: 206px; border-radius: 28px 0 0 28px; }
  .offer-box--right { left: 282px; width: 346px; border-radius: 0 28px 28px 0; }
  .offer-strong { font-weight: 600; font-size: 17px; }
  .offer-note { font-weight: 300; font-size: 13.5px; line-height: 1.15; }

  .audience { top: 627px; font-size: 17px; color: var(--ink); }
  .audience strong { color: #d8141f; font-weight: 700; }
  .booking-pill {
    left: 156px; top: 659px; width: 385px; height: 27px; border-radius: 7px;
    background: var(--deep-red); color: #fff; font-size: 17px; line-height: 27px; text-align: center;
  }
  .addon-intro { top: 696px; font-size: 13px; color: var(--ink); }
  .addon-list {
    top: 707px; font-family: "Playfair Display", serif; font-style: italic; font-weight: 700;
    font-size: 23px; color: var(--deep-red);
  }
  .addon-price { top: 735px; font-size: 17px; color: var(--ink); }

  .photo { top: 780px; width: 152px; height: 90px; border-radius: 8px; }
  .photo--curling { left: 34px; background: linear-gradient(135deg, #6b5c45, #c9a77a 60%, #4c4a3a); }
  .photo--archery { left: 195px; background: linear-gradient(135deg, #8c8a80, #d8d2c4 55%, #6d6a60); }
  .photo--axe { left: 354px; background: linear-gradient(135deg, #2a3f9c 0%, #a83a3a 55%, #7a6a50 100%); }
  .photo--blaster { left: 514px; background: linear-gradient(135deg, #1d2440, #4a3a6a 50%, #2a2a30); }

  .footer-glow {
    left: 0; bottom: 0; width: 360px; height: 60px;
    background: linear-gradient(0deg, rgba(240,150,165,0.6), rgba(255,255,255,0));
  }
  .footer-notes {
    left: 21px; top: 892px; font-weight: 600; font-size: 11.2px; line-height: 13.2px; color: var(--ink-dark);
  }
  .footer-notes p + p { margin-top: 13px; }

  .booking-panel {
    left: 351px; top: 895px; width: 348px; height: 111px;
    background: linear-gradient(160deg, #e00d18 0%, #c8101a 60%, #b81418 100%);
    clip-path: polygon(22% 0, 100% 0, 100% 100%, 0 100%, 11% 18%);
    color: #fff;
  }
  .booking-head { left: 39px; top: 16px; font-weight: 600; font-size: 24px; line-height: 1; }
  .booking-line { left: 39px; font-weight: 600; font-size: 11px; line-height: 1.2; }
  .booking-email {
    left: 39px; top: 64px; font-family: "Playfair Display", serif; font-style: italic;
    font-weight: 700; font-size: 15px; color: var(--email-yellow);
  }
</style>
</head>
<body>
  <main class="flyer">
    <div class="abs garland" role="img" aria-label="Pine branches with red baubles and falling snow"></div>

    <div class="abs center-text script-title">Christmas</div>
    <h1 class="abs center-text main-title">SPECIAL OFFER</h1>

    <section class="abs date-banner">
      <div class="abs banner-pine" role="img" aria-label="Pine sprig decoration"></div>
      <div class="abs banner-glow" role="img" aria-label="Gold festive decoration"></div>
      <div class="abs starts-tab">STARTS</div>
      <div class="abs date-row">
        <span class="date-word">SATURDAY</span>
        <span class="date-day">20th</span>
        <span class="date-word">DECEMBER</span>
      </div>
    </section>

    <div class="abs price">£10PP</div>

    <div class="abs includes-rule" style="left:86px; top:494px; width:151px;"></div>
    <div class="abs includes-rule" style="left:429px; top:494px; width:185px;"></div>
    <div class="abs includes-tick" style="left:86px; top:494px; height:22px;"></div>
    <div class="abs includes-tick" style="left:614px; top:494px; height:22px;"></div>
    <div class="abs includes-label" style="left:237px; width:192px; text-align:center;">OFFER INCLUDES</div>

    <div class="abs offer-box offer-box--left">
      <span class="offer-strong">Half an hour<br>Toboggan track,</span>
    </div>
    <div class="abs offer-box offer-box--right">
      <span class="offer-strong">Half an hour<br>Slingshot paintballs</span>
      <span class="offer-note">(20 paintballs pp) and safe target archery<br>(under cover and indoor ranges).</span>
    </div>

    <p class="abs center-text audience">Activities all the family from &nbsp;<strong>AGE 4 TO GRANDPARENTS</strong> can join in.</p>
    <div class="abs booking-pill">Booking is essential Details on how below.</div>

    <p class="abs center-text addon-intro">Also available &nbsp;Add on indoor activities - including</p>
    <p class="abs center-text addon-list">Mini Curling, Bead Blitz, Safe axe throwing, Air juggler</p>
    <p class="abs center-text addon-price">from £3.50pp and age 6plus.</p>

    <div class="abs photo photo--curling" role="img" aria-label="Photo of players on the mini curling lane"></div>
    <div class="abs photo photo--archery" role="img" aria-label="Photo of the indoor archery range with targets"></div>
    <div class="abs photo photo--axe" role="img" aria-label="Photo of safe throwing axes at a target board"></div>
    <div class="abs photo photo--blaster" role="img" aria-label="Photo of players with blasters in a lit arena"></div>

    <div class="abs footer-glow" role="img" aria-label="Soft pink festive glow decoration"></div>
    <div class="abs footer-notes">
      <p>Café open for hot food and drinks in the<br>‘Fireside Frost Lodge and the heated Christmas marquee.<br>Ages start from 4 plus.</p>
      <p>All activities are great for children and adults so perfect for<br>families as well as friends, parties and get togethers.<br>Free huge car parks.</p>
    </div>

    <section class="abs booking-panel">
      <h2 class="abs booking-head">Booking is Easy</h2>
      <p class="abs booking-line" style="top:43px;">Just Message from our chat (on this post) or email</p>
      <p class="abs booking-email">martin@hollowbrookleisurepark.co.uk</p>
      <p class="abs booking-line" style="top:84px;">for availability of your preferred date and time.</p>
    </section>
  </main>
</body>
</html>
```